Bref créative
VOREN Project
LetterHead, Business Card, Envlp
I need double sided standard sized Business Card [3.5" x 2"]
no certain font requested.
Simple
Serkan OZDIL
Business Development Specialst
Çınarlı Caddesi, Gülbahar Sokak
Korutan İş Merkezi No: 7/214
Kadıköy, İstanbul, Türkiye
so@voren.com.tr
www.voren.com.tr
up to designer
Please use the attached file , all u need is there

```html
<!DOCTYPE html>
<html lang="tr">
<head>
<meta charset="utf-8">
<title>VOREN Project — Stationery</title>
<link href="https://fonts.googleapis.com/css2?family=Roboto:wght@300;400;500&display=swap" rel="stylesheet">
<style>
  :root{
    --page:#ffffff;
    --frame:#d9d9d9;
    --paper:#ffffff;
    --blue-deep:#1a2f8f;
    --blue-mid:#2f55c8;
    --blue-light:#6f9ef0;
    --blue-glow:#9fc4ff;
    --logo:#3a4a6b;
    --ink:#555a66;
    --shadow:rgba(0,0,0,.22);
  }
  *{margin:0;padding:0;box-sizing:border-box}
  html,body{width:1200px;height:741px;overflow:hidden;background:var(--page)}
  body{position:relative;font-family:"Roboto",Arial,sans-serif;color:var(--ink)}
  .frame{position:absolute;left:19px;top:19px;width:1162px;height:702px;border:1px solid var(--frame)}
  .sheet{position:absolute;background:var(--paper);box-shadow:2px 3px 8px var(--shadow);overflow:hidden}
  .band{position:absolute;left:0;top:0;bottom:0;background:linear-gradient(90deg,var(--blue-deep),var(--blue-mid) 55%,var(--blue-light))}
  .brand{position:absolute;display:flex;align-items:center;gap:8px}
  .brand-dot{border-radius:50%;background:var(--blue-mid);border:3px solid var(--paper);box-shadow:0 0 0 2px var(--blue-mid)}
  .brand-name{font-weight:300;color:var(--logo);letter-spacing:.08em}
  .address{position:absolute;font-size:6px;line-height:8.5px;color:var(--ink)}

  /* envelope front */
  .envelope-front{left:60px;top:151px;width:437px;height:209px}
  .envelope-front .band{width:30px}
  .envelope-front .brand{left:14px;top:14px}
  .envelope-front .brand-dot{width:32px;height:32px}
  .envelope-front .brand-name{font-size:24px}
  .envelope-front .address{left:44px;top:56px}

  /* envelope back */
  .envelope-back{left:60px;top:396px;width:437px;height:223px}
  .envelope-back svg{position:absolute;left:0;top:0}

  /* letterhead */
  .letterhead{left:631px;top:86px;width:334px;height:598px}
  .letterhead .band{width:29px}
  .letterhead .brand{left:13px;top:18px}
  .letterhead .brand-dot{width:34px;height:34px}
  .letterhead .brand-name{font-size:24px}
  .letterhead .address{left:70px;top:66px}

  /* business card */
  .card-front{left:972px;top:240px;width:132px;height:70px}
  .card-front .band{width:8px}
  .card-front .brand{left:3px;top:6px;gap:4px}
  .card-front .brand-dot{width:13px;height:13px;border-width:2px;box-shadow:0 0 0 1px var(--blue-mid)}
  .card-front .brand-name{font-size:11px}
  .card-front .person{position:absolute;left:22px;top:32px;font-size:4.5px;line-height:6px}
  .card-front .person strong{font-weight:500;color:var(--logo)}
  .card-back{left:972px;top:324px;width:132px;height:74px;background:radial-gradient(ellipse at 50% 55%,var(--blue-light),var(--blue-mid) 45%,var(--blue-deep))}
  .card-back .emblem{position:absolute;left:50%;top:50%;width:34px;height:34px;margin:-17px 0 0 -17px;border-radius:50%;background:radial-gradient(circle,var(--blue-glow),var(--blue-mid))}
</style>
</head>
<body>
  <div class="frame"></div>

  <section class="sheet envelope-front" aria-label="Envelope front">
    <div class="band"></div>
    <div class="brand"><span class="brand-dot"></span><span class="brand-name">VOREN</span></div>
    <p class="address">Çınarlı Caddesi, Gülbahar Sokak<br>Korutan İş Merkezi No: 7/214<br>Kadıköy, İstanbul, Türkiye</p>
  </section>

  <section class="sheet envelope-back" aria-label="Envelope back">
    <svg width="437" height="223" viewBox="0 0 437 223">
      <defs>
        <linearGradient id="flap" x1="0" y1="0" x2="0" y2="1">
          <stop offset="0" stop-color="#1a2f8f"/>
          <stop offset="1" stop-color="#3a63d4"/>
        </linearGradient>
        <radialGradient id="seal">
          <stop offset="0" stop-color="#9fc4ff"/>
          <stop offset="1" stop-color="#2f55c8"/>
        </radialGradient>
      </defs>
      <polygon points="0,0 437,0 437,14 408,32 248,70 189,70 29,32 0,14" fill="url(#flap)"/>
      <circle cx="218" cy="67" r="17" fill="url(#seal)" stroke="#ffffff" stroke-width="2"/>
    </svg>
  </section>

  <section class="sheet letterhead" aria-label="Letterhead">
    <div class="band"></div>
    <div class="brand"><span class="brand-dot"></span><span class="brand-name">VOREN</span></div>
    <p class="address">Çınarlı Caddesi, Gülbahar Sokak<br>Korutan İş Merkezi No: 7/214<br>Kadıköy, İstanbul, Türkiye<br>Phone: +90 216 555 01 48<br>Fax: +90 216 555 01 49<br>so@voren.com.tr<br>www.voren.com.tr</p>
  </section>

  <section class="sheet card-front" aria-label="Business card front">
    <div class="band"></div>
    <div class="brand"><span class="brand-dot"></span><span class="brand-name">VOREN</span></div>
    <p class="person"><strong>Serkan OZDIL</strong><br>Business Development Specialist<br>Phone: +90 216 555 01 48<br>so@voren.com.tr<br>www.voren.com.tr</p>
  </section>

  <section class="sheet card-back" aria-label="Business card back">
    <span class="emblem"></span>
  </section>
</body>
</html>
```